I am looking for business cards and letterhead

I want a high-level look for CEO's who want a concierge level leadership consultant and organization development strategist

This needs to go with my brand: simple, elegant, clean. Please improve on this design while using these fonts and colors

Here is my website: CorinneValdez.com

```html
<!DOCTYPE html>
<html lang="en">
<head>
<meta charset="utf-8">
<title>Corinne Valdez — Business Card</title>
<link href="https://fonts.googleapis.com/css2?family=Open+Sans:wght@400;600;700&display=swap" rel="stylesheet">
<style>
  :root {
    --backdrop: #2b2e33;
    --card-white: #ffffff;
    --gold: #e2c67f;
    --gold-deep: #d9b96a;
    --brand-blue: #1f5fbf;
    --ink: #3b3d42;
    --ring-white: #ffffff;
  }
  * { box-sizing: border-box; margin: 0; padding: 0; }
  html, body {
    width: 1200px; height: 900px; overflow: hidden;
    background: var(--backdrop);
    font-family: "Open Sans", sans-serif;
  }
  .stage {
    width: 1200px; height: 900px;
    display: flex; align-items: center; justify-content: center; gap: 60px;
  }
  .card {
    width: 520px; height: 300px;
    border-radius: 26px;
    position: relative; overflow: hidden;
    box-shadow: 0 14px 30px rgba(0,0,0,.35);
  }
  /* Front */
  .card-front { background: var(--card-white); }
  .edge-band {
    position: absolute; top: 0; bottom: 0; width: 22px;
    background: var(--gold);
  }
  .edge-band--left { left: 0; }
  .edge-band--right { right: 0; }
  .brand-seal {
    position: absolute; left: 70px; top: 70px;
    width: 150px; height: 150px; border-radius: 50%;
    border: 3px solid var(--gold-deep);
    display: flex; align-items: center; justify-content: center;
    text-align: center;
  }
  .brand-name {
    font-weight: 700; font-size: 19px; line-height: 1.2;
    color: var(--brand-blue);
  }
  .divider {
    position: absolute; left: 252px; top: 62px;
    width: 2px; height: 176px; background: var(--brand-blue);
  }
  .contact-block {
    position: absolute; left: 276px; top: 66px; color: var(--ink);
  }
  .person-name { font-size: 26px; font-weight: 700; line-height: 1.1; }
  .person-name .first { color: var(--brand-blue); }
  .person-name .last { color: var(--ink); }
  .person-title { font-size: 13px; margin-top: 2px; }
  .address { font-size: 13px; line-height: 1.4; margin-top: 12px; }
  .contact-list { list-style: none; margin-top: 10px; font-size: 13px; line-height: 1.55; }
  .contact-list li { display: flex; align-items: center; gap: 8px; }
  .contact-list svg { width: 11px; height: 11px; flex: none; }
  /* Back */
  .card-back {
    background: linear-gradient(160deg, #dcc07a, var(--gold) 55%, #e9d394);
    display: flex; align-items: center; justify-content: center;
  }
  .back-seal {
    width: 190px; height: 190px; border-radius: 50%;
    border: 4px solid var(--ring-white);
    display: flex; align-items: center; justify-content: center; text-align: center;
  }
  .back-seal .brand-name { font-size: 24px; color: var(--brand-blue); }
</style>
</head>
<body>
<main class="stage">
  <section class="card card-front" aria-label="Business card front">
    <div class="edge-band edge-band--left"></div>
    <div class="edge-band edge-band--right"></div>
    <div class="brand-seal"><span class="brand-name">Corinne<br>Valdez</span></div>
    <div class="divider"></div>
    <div class="contact-block">
      <h1 class="person-name"><span class="first">Elena</span> <span class="last">Marsh</span></h1>
      <p class="person-title">CEO</p>
      <p class="address">48 Harbor Lane,<br>Fairview, USA</p>
      <ul class="contact-list">
        <li>
          <svg viewBox="0 0 12 12"><path d="M3 1h2l1 3-1.5 1a6 6 0 0 0 2.5 2.5L8 6l3 1v2a2 2 0 0 1-2 2A8 8 0 0 1 1 3a2 2 0 0 1 2-2z" fill="var(--gold-deep)"/></svg>
          (08) 4410 2368
        </li>
        <li>
          <svg viewBox="0 0 12 12"><rect x="1" y="2.5" width="10" height="7" rx="1" fill="var(--gold-deep)"/><path d="M1.5 3l4.5 3.5L10.5 3" stroke="#fff" fill="none"/></svg>
          info@CorinneValdez.com
        </li>
        <li>
          <svg viewBox="0 0 12 12"><circle cx="6" cy="6" r="5" fill="var(--gold-deep)"/><path d="M1 6h10M6 1c-2 3-2 7 0 10M6 1c2 3 2 7 0 10" stroke="#fff" stroke-width=".8" fill="none"/></svg>
          www.CorinneValdez.com
        </li>
      </ul>
    </div>
  </section>

  <section class="card card-back" aria-label="Business card back">
    <div class="back-seal"><span class="brand-name">Corinne<br>Valdez</span></div>
  </section>
</main>
</body>
</html>
```